50th Anniversary Gala Save the date Postcard 8.5x5.5 inches

Looking for a 5.5x8.5 in one-sided postcard design for our annual gala. Design needs to include "Save the date" prominently with all the event information included below. Design should be light, include the colors of our logo and elegant. (almost like a wedding save the date). "Bridges of Grace" should look like its own logo.

50th Anniversary Gala at The Lodge at Birchmere Glen – “Bridges of Grace – Celebrating 50 Years of Building Community”
Thursday, October 24
6-11p
The Lodge at Birchmere Glen
Calloway Parkway, New Hyde Park, NY
Honoring – TRB Previous Presidents

Target Market(s)

Exisiting donors

Industry/Entity Type

nonprofit

Font styles to use
Serif
Script

Requirements
Must have
• Save the date prominent
Should not have
• should not have a dark background

```html
<!DOCTYPE html>
<html lang="en">
<head>
<meta charset="utf-8">
<title>Save the Date – 50th Anniversary Gala</title>
<link rel="stylesheet" href="https://fonts.googleapis.com/css2?family=Great+Vibes&family=Montserrat:ital,wght@0,400;0,600;0,700;0,800;1,600&family=Allura&display=swap">
<style>
  :root {
    --page: #ffffff;
    --card: #dcd0bd;
    --frame: #ffffff;
    --ink: #111111;
    --navy: #1f4587;
    --sky: #1b8fd4;
    --gold: #d9ad45;
  }
  * { margin: 0; padding: 0; box-sizing: border-box; }
  html, body { width: 1200px; height: 1200px; overflow: hidden; background: var(--page); }
  body { position: relative; font-family: "Montserrat", sans-serif; color: var(--ink); }

  .postcard {
    position: absolute; left: 231px; top: 28px; width: 745px; height: 1151px;
    background: var(--card); overflow: hidden;
  }
  .foliage { position: absolute; }
  .foliage--left {
    left: 0; top: 0; width: 420px; height: 640px;
    background:
      radial-gradient(ellipse 190px 110px at 170px 40px, rgba(90,74,44,.7), transparent),
      radial-gradient(ellipse 170px 260px at 110px 300px, rgba(160,146,120,.5), transparent),
      radial-gradient(ellipse 120px 160px at 50px 480px, rgba(170,156,132,.35), transparent);
    -webkit-mask-image: linear-gradient(to bottom, #000 60%, transparent 100%);
    mask-image: linear-gradient(to bottom, #000 60%, transparent 100%);
  }
  .foliage--right {
    right: 0; top: 0; width: 260px; height: 440px;
    background:
      radial-gradient(ellipse 130px 110px at 140px 60px, rgba(90,74,44,.75), transparent),
      radial-gradient(ellipse 80px 150px at 240px 290px, rgba(80,62,40,.7), transparent);
    -webkit-mask-image: linear-gradient(to bottom, #000 70%, transparent 100%);
    mask-image: linear-gradient(to bottom, #000 70%, transparent 100%);
  }
  .frame {
    position: absolute; left: 25px; top: 34px; width: 695px; height: 1085px;
    border: 3px solid var(--frame);
  }

  .headline__save, .headline__the, .headline__date { position: absolute; line-height: 1; font-weight: 400; }
  .headline__save {
    left: 190px; top: 185px;
    font-family: "Great Vibes", cursive; font-size: 140px;
  }
  .headline__the {
    left: 452px; top: 268px;
    font-family: "Montserrat", sans-serif; font-weight: 800; font-size: 36px; letter-spacing: 1px;
  }
  .headline__date {
    left: 292px; top: 282px;
    font-family: "Great Vibes", cursive; font-size: 140px;
  }

  .gala-title {
    position: absolute; left: 0; top: 498px; width: 745px; text-align: center;
    color: var(--navy); font-weight: 700; font-size: 21px; line-height: 29px;
  }
  .gala-title__rule { display: inline-block; width: 38px; height: 1.5px; background: var(--navy); vertical-align: middle; }

  .theme-mark {
    position: absolute; left: 0; top: 592px; width: 745px; text-align: center;
    color: var(--sky); font-family: "Allura", cursive;
  }
  .theme-mark__top { display: block; font-size: 90px; line-height: 1; }
  .theme-mark__bottom { display: block; font-size: 96px; line-height: .9; margin-left: 60px; }

  .tagline {
    position: absolute; left: 0; top: 836px; width: 745px; text-align: center;
    font-weight: 700; font-size: 17px;
  }

  .details { position: absolute; left: 201px; top: 872px; display: flex; align-items: center; }
  .details__when { font-size: 15px; line-height: 19px; padding-right: 14px; border-right: 1px solid var(--ink); }
  .details__when strong { font-weight: 700; font-size: 16px; display: block; }
  .details__where { font-size: 13px; line-height: 17px; padding-left: 15px; }

  .org-name {
    position: absolute; left: 0; top: 978px; width: 745px;
    display: flex; justify-content: center; align-items: center; gap: 10px;
    color: var(--navy); font-weight: 700; font-size: 18px; letter-spacing: .5px;
  }
  .org-name__dot { width: 14px; height: 14px; border-radius: 50%; background: var(--gold); }

  .honoring {
    position: absolute; left: 22px; top: 1068px; width: 745px; text-align: center;
    color: var(--navy); font-style: italic; font-weight: 600; font-size: 20px;
  }
</style>
</head>
<body>
  <main class="postcard">
    <div class="foliage foliage--left" role="img" aria-label="Painted botanical leaves and white blossoms in olive, bronze and cream"></div>
    <div class="foliage foliage--right" role="img" aria-label="Painted olive and brown leaves with a white blossom"></div>
    <div class="frame"></div>

    <h1 class="headline">
      <span class="headline__save">Save</span>
      <span class="headline__the">THE</span>
      <span class="headline__date">date</span>
    </h1>

    <p class="gala-title">
      <span class="gala-title__rule"></span>50th Anniversary Gala<span class="gala-title__rule"></span><br>
      at The Lodge at Birchmere Glen
    </p>

    <p class="theme-mark">
      <span class="theme-mark__top">Bridges of</span>
      <span class="theme-mark__bottom">Grace</span>
    </p>

    <p class="tagline">Celebrating 50 Years of Building Community</p>

    <div class="details">
      <p class="details__when"><strong>Thursday,</strong>October 24<br>6-11pm</p>
      <p class="details__where">The Lodge at Birchmere Glen<br>Calloway Parkway, New Hyde Park, NY</p>
    </div>

    <p class="org-name"><span class="org-name__dot"></span>Tri-River Bridges</p>

    <p class="honoring">Honoring – TRB Previous Presidents</p>
  </main>
</body>
</html>
```